Briney Lark Fare landing page design

We need a landing page designed for an ecommerce website that sales fresh US domestic shrimp from the Gulf of Mexico and ships them direct to the consumer "From Our Shore To Your Door". For the landing page, we would like customers to be able to place an order and or inquire further about our product as well as links to social media. The company logo is attached

1 page

```html
<!DOCTYPE html>
<html lang="en">
<head>
<meta charset="utf-8">
<title>Briney Lark Fare – Wild Gulf Shrimp</title>
<link href="https://fonts.googleapis.com/css2?family=Poppins:wght@300;400;500;600;700&family=Open+Sans:wght@400;600&display=swap" rel="stylesheet">
<style>
:root{
  --orange:#ef7f4a;
  --steel:#7f9db5;
  --ink:#222222;
  --muted:#777777;
  --light:#b9c3cc;
  --dark:#0c0c0c;
  --white:#ffffff;
  --shrimp-a:#e9875a;
  --brown-a:#4a2b20;
  --brown-b:#2a1914;
}
*{box-sizing:border-box;margin:0;padding:0}
html,body{width:1200px;height:2521px;overflow:hidden}
body{position:relative;background:var(--white);font-family:"Open Sans",sans-serif;color:var(--ink)}
.abs{position:absolute}
a{color:inherit;text-decoration:none}

/* header */
.site-header{left:0;top:0;width:1200px;height:69px;background:var(--white)}
.brand{display:flex;align-items:center;gap:10px;font-family:"Poppins",sans-serif;font-weight:600;color:var(--ink)}
.brand-mark{border:2px solid var(--light);border-radius:50%}
.header-brand{left:213px;top:8px;font-size:20px}
.header-brand .brand-mark{width:52px;height:52px}
.main-nav{left:551px;top:30px;display:flex;gap:16px;font-family:"Poppins",sans-serif;font-size:10px;line-height:12px;color:#444;text-transform:uppercase;white-space:nowrap}
.social{display:flex;gap:8px}
.social span{width:25px;height:25px;border-radius:50%;background:var(--steel);display:block}
.header-social{left:857px;top:24px}

/* hero */
.hero{left:0;top:69px;width:1200px;height:385px;background:radial-gradient(ellipse at 50% 45%,#c9754c,#a3522f 55%,#6f3520)}
.hero-curve{left:0;top:420px;width:1200px;height:40px}
.hero-mark{left:533px;top:101px;width:134px;height:134px;border:2px solid rgba(255,255,255,.85);border-radius:50%;display:flex;align-items:center;justify-content:center}
.hero-mark span{width:104px;height:104px;border-radius:50%;background:var(--white);display:flex;align-items:center;justify-content:center;font-family:"Poppins",sans-serif;font-weight:600;font-size:12px;color:var(--ink);text-align:center;line-height:1.2}
.hero-kicker{left:0;top:246px;width:1200px;text-align:center;font-family:"Poppins",sans-serif;font-weight:300;font-size:24px;color:var(--white)}
.hero-title{left:0;top:274px;width:1200px;text-align:center;font-family:"Poppins",sans-serif;font-weight:600;font-size:33px;color:var(--white)}
.btn{display:inline-block;background:var(--steel);color:var(--white);font-family:"Poppins",sans-serif;font-weight:600;font-size:10px;text-transform:uppercase;border-radius:14px;text-align:center}
.hero-btn{left:556px;top:336px;width:88px;height:28px;line-height:28px}
.scroll-down{left:577px;top:453px;width:46px;height:46px;border-radius:50%;background:var(--white);box-shadow:0 3px 10px rgba(0,0,0,.18);display:flex;align-items:center;justify-content:center}

/* welcome */
.welcome-photo{left:227px;top:504px;width:277px;height:227px;border-radius:40%;background:radial-gradient(ellipse,var(--shrimp-a) 30%,#f2c4ad 60%,#fff 75%)}
.welcome-kicker{left:620px;top:524px;font-family:"Poppins",sans-serif;font-size:20px;color:var(--ink)}
.welcome-title{left:620px;top:548px;font-family:"Poppins",sans-serif;font-weight:400;font-size:29px;color:var(--ink)}
.welcome-title em{font-style:normal;color:var(--light)}
.welcome-text{left:620px;top:605px;width:316px;font-size:10.5px;line-height:16.5px;color:var(--muted)}
.welcome-btn{left:619px;top:686px;width:87px;height:28px;line-height:28px}

/* feature bar */
.feature-bar{left:235px;top:778px;width:731px;height:75px;background:var(--white);box-shadow:0 2px 10px rgba(0,0,0,.12);display:flex;z-index:2}
.feature{flex:1;text-align:center;padding-top:13px;font-family:"Poppins",sans-serif;border-left:1px solid #e6e6e6}
.feature:first-child{border-left:none}
.feature svg{display:block;margin:0 auto 4px}
.feature b{display:block;font-size:9.5px;font-weight:600;text-transform:uppercase}
.feature small{font-size:9.5px;color:#444}

/* dark sections */
.dark-band{left:0;width:1200px;background:radial-gradient(ellipse at 50% 50%,var(--brown-a),var(--brown-b) 75%,#1b100c)}
.delivery{top:818px;height:446px}
.section-title{left:0;width:1200px;text-align:center;font-family:"Poppins",sans-serif;font-weight:500;font-size:28px}
.rule{left:576px;width:48px;height:2px;background:var(--orange)}
.step-ring{width:100px;height:100px;border-radius:50%;border:1.5px solid rgba(255,255,255,.7);display:flex;align-items:center;justify-content:center}
.step-ring span{width:70px;height:70px;border-radius:50%;background:var(--white);display:flex;align-items:center;justify-content:center}
.step-label{width:220px;text-align:center;font-family:"Poppins",sans-serif;color:var(--white);font-size:11px;line-height:16px}
.step-label b{font-weight:600;display:block}

/* products */
.card{width:169px;height:192px;border:1.5px solid #f0a27d;background:var(--white);text-align:center;font-family:"Poppins",sans-serif}
.card-photo{width:130px;height:110px;margin:20px auto 10px;border-radius:50%;background:radial-gradient(ellipse,var(--shrimp-a) 25%,#f6d6c6 60%,#fff 72%)}
.card-name{font-size:12px;color:#333}
.card-price{font-size:12.5px;color:var(--ink)}
.card-price s{font-size:10px;color:#aaa;margin-left:4px}

/* why choose */
.why{top:1868px;height:346px}
.why-mark{left:536px;top:1994px;width:128px;height:128px;border-radius:50%;border:1.5px solid rgba(255,255,255,.75);display:flex;align-items:center;justify-content:center}
.why-mark span{width:100px;height:100px;border-radius:50%;border:1.5px solid rgba(255,255,255,.5)}
.why-item{width:240px;font-family:"Poppins",sans-serif;color:var(--white)}
.why-item b{display:block;font-size:12px;font-weight:600;margin-bottom:4px}
.why-item p{font-size:10.5px;line-height:15px;color:#ddd}
.why-left{text-align:right}

/* footer */
.footer-brand{left:230px;top:2238px;font-size:20px}
.footer-brand .brand-mark{width:50px;height:50px}
.contact-line{left:235px;font-size:10.5px;color:#555}
.footer-social{left:235px;top:2367px}
.footer-social span{width:22px;height:22px;background:#e9e9e9}
.footer-social span:nth-child(2){background:#444}
.footer-col{font-family:"Poppins",sans-serif}
.footer-col h4{font-size:10px;font-weight:600;text-transform:uppercase;margin-bottom:13px}
.footer-col li{list-style:none;font-size:10.5px;color:#555;margin-bottom:8px;font-family:"Open Sans",sans-serif}
.footer-col li.active{color:var(--orange)}
.to-top{left:985px;top:2369px;width:31px;height:31px;border-radius:50%;background:var(--orange);display:flex;align-items:center;justify-content:center}

/* newsletter */
.newsletter{left:0;top:2424px;width:1200px;height:76px;background:var(--dark)}
.news-title{left:235px;top:2444px;font-family:"Poppins",sans-serif;font-weight:600;font-size:13px;color:var(--white)}
.news-text{left:235px;top:2464px;font-size:10px;color:#ddd}
.news-form{left:716px;top:2448px;width:248px;height:29px;display:flex;border-radius:15px;overflow:hidden}
.news-input{flex:1;background:var(--white);font-size:10px;color:#666;padding:8px 14px}
.news-btn{width:82px;background:var(--orange);color:var(--white);font-family:"Poppins",sans-serif;font-size:9px;text-transform:uppercase;text-align:center;line-height:29px}

.legal{left:235px;top:2508px;font-size:8.5px;color:#666}
.pay{left:786px;top:2506px;display:flex;gap:6px}
.pay span{width:24px;height:12px;border-radius:2px;background:#6c7fb4}
.pay span:nth-child(2){background:#d7d7d7}
.pay span:nth-child(3){background:#8fb2dd}
.pay span:nth-child(5){background:#e69a4d}
</style>
</head>
<body>

<header class="site-header abs">
  <div class="brand header-brand abs"><span class="brand-mark"></span>Briney Lark Fare</div>
  <nav class="main-nav abs">
    <a href="#">Home</a><a href="#">Shop</a><a href="#">Products</a><a href="#">Aboutus</a><a href="#">Contact</a>
  </nav>
  <div class="social header-social abs" aria-label="Social media links"><span></span><span></span><span></span><span></span></div>
</header>

<section class="hero abs" role="img" aria-label="Photograph of fresh wild Gulf shrimp piled on ice"></section>
<svg class="hero-curve abs" viewBox="0 0 1200 40" preserveAspectRatio="none" aria-hidden="true">
  <path d="M0 12 Q600 46 1200 12 L1200 40 L0 40 Z" fill="#ffffff"/>
</svg>
<div class="hero-mark abs"><span>Briney<br>Lark Fare</span></div>
<p class="hero-kicker abs">We represent the finest</p>
<h1 class="hero-title abs">Wild Shrimp from the U.S. Gulf</h1>
<a class="btn hero-btn abs" href="#">Shop now</a>
<div class="scroll-down abs">
  <svg width="10" height="8" viewBox="0 0 10 8"><path d="M0 0 L10 0 L5 8 Z" fill="#222"/></svg>
</div>

<div class="welcome-photo abs" role="img" aria-label="Photograph of a heap of cooked pink shrimp"></div>
<p class="welcome-kicker abs">Welcome To</p>
<h2 class="welcome-title abs">BRINEY LARK <em>FARE</em></h2>
<p class="welcome-text abs">Sed quia non numquam modi tempora indunt ut labore et dolore magnam aliquam quaerat a non numquam modi tempora indunt ut labore et dolore magnam aliquam magnam aliquam quaerat a non numquam</p>
<a class="btn welcome-btn abs" href="#">Shop now</a>

<section class="dark-band delivery abs" role="img" aria-label="Dim photograph of raw shrimp"></section>
<div class="feature-bar abs">
  <div class="feature">
    <svg width="20" height="14" viewBox="0 0 20 14" fill="none" stroke="#ef7f4a" stroke-width="1.3"><rect x="1" y="2" width="11" height="8"/><path d="M12 5h4l3 3v2h-7"/><circle cx="5" cy="12" r="1.5"/><circle cx="15" cy="12" r="1.5"/></svg>
    <b>Free Shipping</b><small>For all order over 99$</small>
  </div>
  <div class="feature">
    <svg width="16" height="16" viewBox="0 0 16 16" fill="none" stroke="#ef7f4a" stroke-width="1.3"><circle cx="8" cy="8" r="6.5"/><path d="M8 4v4l3 2"/></svg>
    <b>Delivery on time</b><small>If good have prolems</small>
  </div>
  <div class="feature">
    <svg width="20" height="14" viewBox="0 0 20 14" fill="none" stroke="#ef7f4a" stroke-width="1.3"><rect x="1" y="1" width="18" height="12" rx="2"/><path d="M1 5h18"/></svg>
    <b>Secure Payment</b><small>100% secure payment</small>
  </div>
</div>

<h2 class="section-title abs" style="top:918px;color:#fff">Delivery Process</h2>
<div class="rule abs" style="top:965px"></div>
<svg class="abs" style="left:180px;top:1040px" width="840" height="110" viewBox="0 0 840 110" aria-hidden="true">
  <path d="M14 94 C50 82 80 70 104 64 M204 50 C270 36 320 28 366 26 M466 30 C530 45 580 65 630 68 M730 66 C770 60 800 45 832 23" fill="none" stroke="#fff" stroke-width="1.3" stroke-dasharray="5 4"/>
  <circle cx="14" cy="94" r="3" fill="#fff"/>
  <path d="M832 23 l-9 1 M832 23 l-3 8" stroke="#fff" stroke-width="1.3"/>
</svg>
<div class="step-ring abs" style="left:284px;top:1034px"><span role="img" aria-label="Small shrimp illustration"><svg width="40" height="22"><ellipse cx="20" cy="11" rx="17" ry="7" fill="#ef7f4a"/></svg></span></div>
<div class="step-label abs" style="left:224px;top:1144px"><b>STEP 01</b>Choose Your Products</div>
<div class="step-ring abs" style="left:546px;top:1017px"><span><svg width="24" height="32" viewBox="0 0 26 34"><path d="M13 1C6 1 1 6 1 13c0 9 12 20 12 20s12-11 12-20C25 6 20 1 13 1z" fill="#ef7f4a"/><circle cx="13" cy="13" r="4.5" fill="#fff"/></svg></span></div>
<div class="step-label abs" style="left:486px;top:1124px"><b>STEP 03</b>Share Your Location</div>
<div class="step-ring abs" style="left:810px;top:1059px"><span><svg width="36" height="26" viewBox="0 0 40 28" fill="none" stroke="#ef7f4a" stroke-width="1.8"><rect x="10" y="4" width="18" height="15"/><path d="M28 9h6l4 5v5H28"/><circle cx="16" cy="23" r="3"/><circle cx="33" cy="23" r="3"/><circle cx="8" cy="10" r="6" fill="#fff"/><path d="M8 7v3h2"/></svg></span></div>
<div class="step-label abs" style="left:750px;top:1170px"><b>STEP 04</b>Get Delivered Fast</div>

<h2 class="section-title abs" style="top:1302px;color:#222">Featured Product</h2>
<div class="rule abs" style="top:1356px"></div>

<div class="card abs" style="left:235px;top:1401px"><div class="card-photo" role="img" aria-label="Product photo of red shrimp"></div><p class="card-name">Product name</p><p class="card-price">$14.00<s>$35.00</s></p></div>
<div class="card abs" style="left:422px;top:1401px"><div class="card-photo" role="img" aria-label="Product photo of a peeled shrimp"></div><p class="card-name">Product name</p><p class="card-price">$14.00<s>$35.00</s></p></div>
<div class="card abs" style="left:609px;top:1401px"><div class="card-photo" role="img" aria-label="Product photo of a raw brown shrimp"></div><p class="card-name">Product name</p><p class="card-price">$14.00<s>$35.00</s></p></div>
<div class="card abs" style="left:797px;top:1401px"><div class="card-photo" role="img" aria-label="Product photo of three red prawns"></div><p class="card-name">Product name</p><p class="card-price">$14.00<s>$35.00</s></p></div>
<div class="card abs" style="left:235px;top:1623px"><div class="card-photo" role="img" aria-label="Product photo of a raw brown shrimp"></div><p class="card-name">Product name</p><p class="card-price">$14.00<s>$35.00</s></p></div>
<div class="card abs" style="left:422px;top:1623px"><div class="card-photo" role="img" aria-label="Product photo of three red prawns"></div><p class="card-name">Product name</p><p class="card-price">$14.00<s>$35.00</s></p></div>
<div class="card abs" style="left:609px;top:1623px"><div class="card-photo" role="img" aria-label="Product photo of red shrimp"></div><p class="card-name">Product name</p><p class="card-price">$14.00<s>$35.00</s></p></div>
<div class="card abs" style="left:797px;top:1623px"><div class="card-photo" role="img" aria-label="Product photo of a peeled shrimp"></div><p class="card-name">Product name</p><p class="card-price">$14.00<s>$35.00</s></p></div>

<section class="dark-band why abs" role="img" aria-label="Dim close-up photograph of shrimp"></section>
<h2 class="section-title abs" style="top:1926px;color:#fff;font-size:22px">Why Choose Us</h2>
<div class="rule abs" style="top:1961px"></div>
<div class="why-mark abs"><span></span></div>
<div class="why-item why-left abs" style="left:246px;top:1999px"><b>Eat Healthier</b><p>Modi temporq incidunt ut<br>labore dolore magnam ali-</p></div>
<div class="why-item why-left abs" style="left:246px;top:2075px"><b>We Have Brands</b><p>Modi temporq incidunt ut<br>labore dolore magnam ali-</p></div>
<div class="why-item abs" style="left:707px;top:1996px"><b>Fresh And Clean Products</b><p>Modi tempora incidunt ut<br>labore dolore magnam ali-</p></div>
<div class="why-item abs" style="left:707px;top:2071px"><b>Modern Process</b><p>Modi tempora incidunt ut<br>labore dolore magnam ali-</p></div>

<footer>
  <div class="brand footer-brand abs"><span class="brand-mark"></span>Briney Lark Fare</div>
  <p class="contact-line abs" style="top:2298px">Address: 14 Harbor Row, Pelican Bay</p>
  <p class="contact-line abs" style="top:2320px">Phone: +00 555 0142</p>
  <p class="contact-line abs" style="top:2342px">Email: hello@brineylarkfare.com</p>
  <div class="social footer-social abs"><span></span><span></span><span></span><span></span></div>

  <div class="footer-col abs" style="left:522px;top:2266px"><h4>Information</h4><ul><li>About Us</li><li>Checkout</li><li>Contact</li><li>Sorivius</li></ul></div>
  <div class="footer-col abs" style="left:697px;top:2266px"><h4>My Account</h4><ul><li class="active">My Account</li><li>Contact</li><li>Shopping Cart</li><li>Shop</li></ul></div>
  <div class="footer-col abs" style="left:899px;top:2266px"><h4>Quick Shop</h4><ul><li>Shipping &amp; Returns</li><li>Contact</li><li>Secure Shopping</li><li>Affiliates</li></ul></div>
  <div class="to-top abs"><svg width="10" height="6" viewBox="0 0 10 6"><path d="M1 5 L5 1 L9 5" fill="none" stroke="#fff" stroke-width="1.3"/></svg></div>

  <div class="newsletter abs"></div>
  <p class="news-title abs">Join Our Newsletter Now</p>
  <p class="news-text abs">Get E-mail updates about our latest shop and special offers.</p>
  <div class="news-form abs"><span class="news-input">Enter your mail</span><span class="news-btn">Subscribe</span></div>

  <p class="legal abs">Copyright © 2019 brineylarkfare.com All Rights Reserved.</p>
  <div class="pay abs" aria-label="Accepted payment methods"><span></span><span></span><span></span><span></span><span></span><span></span></div>
</footer>

</body>
</html>
```